Web Design Project for Velorasa cloud based service

None of us is a designer, and ENGLISH is not our first language, but we need to make sure that those bidding for this project understand that we're just looking for the creative components in order to build a website and we don't need you to create all the pages and /or diagram the website for us. Please ask as many questions as you want for us to ensure we don't waste your time.

Content and Community Management System
- We need a redesign of the Back Office Screens
o The kind of screen detailed on the (file 2 attached bellow) “Velorasa Some Screens.pptx”
- Following, as a strong reference te velorasa logo design line (file 1 attached bellow)
- We DO NOT need application, or implementation, only the following SOW.

Scope of Work (SOW) by components that we need:
- Main Theme
- Tables
- Buttons
- Icons
- Lists
- Form elements

OUT of Scope (we DO NOT need it):
· Emerging Windows implementation (jquery – lightbox)
· Layout (we do not need you to create the layout for us)
· Module Development (Css 3, jQuery, Html 5)

Reason: We're extending the deadline in order to have more options to select. The current option do not fit our expectation yet. Any question, please do it. Many thanks. Velorasa Team.

Hi designers!

We've [a] extended the deadline in order to have more choices and we made a change on the Power Point file attached with [b] the 3 most important screen than include all the components/element we need designed from you.

We wait for your proposal.
Let's do it!

Many Thanks.
Best regards.

velorasa Team.

```html
<!DOCTYPE html>
<html lang="es">
<head>
<meta charset="utf-8">
<title>Velorasa – Panel de administración</title>
<link href="https://fonts.googleapis.com/css2?family=Cabin:wght@400;500;600;700&display=swap" rel="stylesheet">
<style>
  :root {
    --page-bg: #e6e7e9;
    --panel-bg: #ffffff;
    --panel-border: #d2d3d6;
    --nav-bg: #3b3c3e;
    --nav-text: #ffffff;
    --ink: #1d2340;
    --ink-soft: #2b2b2b;
    --accent: #8a1d3c;
    --card-top: #ffffff;
    --card-bottom: #ececec;
    --card-border: #d6d6d8;
    --brand-square: #1d2340;
  }
  * { box-sizing: border-box; margin: 0; padding: 0; }
  html, body {
    width: 1200px; height: 620px; overflow: hidden;
    background: var(--page-bg);
    font-family: "Cabin", "Helvetica Neue", Arial, sans-serif;
    color: var(--ink);
  }
  .canvas { position: relative; width: 1200px; height: 620px; }

  .brand {
    position: absolute; left: 168px; top: 96px;
    display: flex; align-items: center; gap: 10px;
  }
  .brand-square { width: 22px; height: 22px; background: var(--brand-square); }
  .brand-name {
    font-weight: 700; font-size: 30px; letter-spacing: 0.5px;
    color: var(--ink); text-transform: uppercase;
  }

  .main-nav {
    position: absolute; left: 434px; top: 60px;
    display: flex; gap: 6px; list-style: none;
  }
  .main-nav a {
    display: flex; align-items: center; justify-content: center;
    width: 96px; height: 34px; border-radius: 6px;
    background: var(--nav-bg); color: var(--nav-text);
    font-size: 13px; text-decoration: none;
  }

  .status-bar {
    position: absolute; left: 168px; top: 157px; width: 873px; height: 39px;
    background: var(--panel-bg); border: 1px solid var(--panel-border); border-radius: 8px;
    display: flex; align-items: center; justify-content: space-between;
    padding: 0 16px 0 28px;
  }
  .project-label { font-size: 15px; color: var(--ink); }
  .user-links { font-size: 12px; color: var(--ink-soft); }

  .dashboard {
    position: absolute; left: 168px; top: 207px; width: 873px; height: 392px;
    background: var(--panel-bg); border: 1px solid var(--panel-border); border-radius: 8px;
  }
  .section-title {
    position: absolute; font-weight: 400; font-size: 20px; color: var(--accent);
  }
  .sections-title { left: 32px; top: 27px; }
  .goto-title { left: 645px; top: 27px; }

  .section-grid {
    position: absolute; left: 13px; top: 78px;
    display: grid; grid-template-columns: repeat(3, 194px); grid-auto-rows: 124px;
    column-gap: 7px; row-gap: 9px;
  }
  .section-card {
    border: 1px solid var(--card-border); border-radius: 6px;
    background: linear-gradient(var(--card-top) 45%, var(--card-bottom));
    padding: 14px 13px 0 13px;
  }
  .section-card h3 { font-weight: 500; font-size: 15px; color: var(--ink); margin-bottom: 7px; }
  .section-card p {
    font-size: 11px; line-height: 17px; color: var(--ink-soft); text-align: justify;
  }

  .goto-list {
    position: absolute; left: 651px; top: 80px; list-style: none;
  }
  .goto-list li { font-size: 12.5px; line-height: 27px; color: var(--ink-soft); }
</style>
</head>
<body>
<div class="canvas">
  <header>
    <div class="brand">
      <span class="brand-square"></span>
      <span class="brand-name">Velorasa</span>
    </div>
    <nav>
      <ul class="main-nav">
        <li><a href="#">Escritorto</a></li>
        <li><a href="#">Paginas</a></li>
        <li><a href="#">Modulos</a></li>
        <li><a href="#">Picheros</a></li>
        <li><a href="#">Administration</a></li>
        <li><a href="#">Live Site</a></li>
      </ul>
    </nav>
  </header>

  <div class="status-bar">
    <span class="project-label">Proyecto : Region : BRASIL</span>
    <span class="user-links">Usuertio : Admin | Preferencias &nbsp;| Perfill &nbsp;| Salir</span>
  </div>

  <main class="dashboard">
    <h2 class="section-title sections-title">Secciones principales</h2>
    <div class="section-grid">
      <article class="section-card"><h3>Escritorio</h3><p>It is a long established fact that a reader will be distracted by the readable content of a page when looking at its layout...</p></article>
      <article class="section-card"><h3>Paginas</h3><p>It is a long established fact that a reader will be distracted by the readable content of a page when looking at its layout...</p></article>
      <article class="section-card"><h3>Modulos</h3><p>It is a long established fact that a reader will be distracted by the readable content of a page when looking at its layout...</p></article>
      <article class="section-card"><h3>Ficheros</h3><p>It is a long established fact that a reader will be distracted by the readable content of a page when looking at its layout...</p></article>
      <article class="section-card"><h3>Administraction</h3><p>It is a long established fact that a reader will be distracted by the readable content of a page when looking at its layout...</p></article>
      <article class="section-card"><h3>Sitio en produccion</h3><p>It is a long established fact that a reader will be distracted by the readable content of a page when looking at its layout...</p></article>
    </div>

    <h2 class="section-title goto-title">Ir A</h2>
    <ul class="goto-list">
      <li>Nieva Pagina</li>
      <li>Nuevo usuario</li>
      <li>Nuevo ContenIdo</li>
      <li>Nieva Pagina</li>
      <li>Nuevo usuario</li>
      <li>Nuevo ContenIdo</li>
      <li>Nieva Pagina</li>
      <li>Nuevo usuario</li>
      <li>Nuevo ContenIdo</li>
      <li>Nieva Pagina</li>
    </ul>
  </main>
</div>
</body>
</html>
```